Front & Back cover design for timber flooring brochure - A4 size

I need a design for the front and back cover of an A4 sized brochure for a timber and concrete flooring company called "Grand Oak Surfaces". The front cover should include the logo (attached), and an image + tagline for each of the three products/services that they offer which are:

1. Timber Flooring
2. Concrete Grinding & Sealing
3. Floor sanding (i have attached a photo for each of these three - however feel free to use other images if you feel they are better).

The back cover should be simple, perhaps just a continuation of the colour or graphic scheme on the front with the company contact details at the bottom.

Industry/Entity Type

Flooring

Requirements
Must have
• front cover has to have the logo with an image and text of the 3 services described. You can use the images attached or your own.

```html
<!DOCTYPE html>
<html lang="en">
<head>
<meta charset="utf-8">
<title>Grand Oak Surfaces – Brochure Covers</title>
<link href="https://fonts.googleapis.com/css2?family=Orbitron:wght@500&family=Open+Sans:wght@300&family=Cinzel:wght@600&display=swap" rel="stylesheet">
<style>
  :root {
    --page-bg: #ffffff;
    --brand-gold: #a8741a;
    --wood-light: #e7a24e;
    --wood-mid: #c97a2c;
    --wood-deep: #8a4414;
    --wood-dark: #2a0f05;
    --heading-ink: #120a04;
    --body-ink: #fff8ee;
    --tile-red: #7a3a44;
    --tile-rose: #c08c92;
    --concrete: #6b6f5c;
    --concrete-light: #9aa08a;
    --sanded-red: #a8441c;
    --sanded-light: #d9753a;
  }
  html, body {
    margin: 0;
    padding: 0;
    overflow: hidden;
  }
  body {
    width: 858px;
    height: 1200px;
    position: relative;
    background: var(--page-bg);
  }
  .brand {
    position: absolute;
    left: 85px;
    top: 42px;
    width: 460px;
    display: flex;
    align-items: center;
    gap: 14px;
  }
  .brand-mark {
    width: 36px;
    height: 36px;
    background: var(--brand-gold);
    flex: none;
  }
  .brand-name {
    font-family: "Cinzel", serif;
    font-weight: 600;
    font-size: 38px;
    color: var(--brand-gold);
    white-space: nowrap;
    letter-spacing: 1px;
  }

  .cover {
    position: absolute;
    overflow: hidden;
  }
  .cover-art {
    position: absolute;
    inset: 0;
  }
  .cover--back {
    left: 232px;
    top: 328px;
    width: 626px;
    height: 872px;
    z-index: 1;
    box-shadow: 0 0 14px rgba(150, 90, 40, 0.45);
  }
  .cover--back .cover-art {
    background:
      linear-gradient(90deg, transparent 62%, rgba(90, 25, 10, 0.55) 70%, transparent 76%),
      linear-gradient(180deg, var(--wood-light) 0%, var(--wood-mid) 45%, var(--wood-deep) 80%, var(--wood-dark) 100%);
  }
  .cover--front {
    left: 10px;
    top: 140px;
    width: 608px;
    height: 725px;
    z-index: 2;
    box-shadow: 0 0 16px rgba(120, 70, 30, 0.55);
  }
  .cover--front .cover-art {
    background:
      radial-gradient(ellipse 80% 30% at 50% 72%, rgba(255, 190, 120, 0.25), transparent 70%),
      linear-gradient(180deg, #d9923f 0%, var(--wood-light) 30%, var(--wood-mid) 60%, var(--wood-deep) 80%, var(--wood-dark) 100%);
  }

  .title,
  .service-name,
  .section-title {
    font-family: "Orbitron", sans-serif;
    font-weight: 500;
    color: var(--heading-ink);
    text-transform: uppercase;
    margin: 0;
    position: absolute;
  }
  .title {
    left: 8px;
    top: 48px;
    font-size: 30px;
    letter-spacing: 5px;
  }
  .service-name {
    left: 45px;
    font-size: 15px;
    letter-spacing: 4px;
    line-height: 24px;
  }
  .service-name--timber { top: 108px; }
  .service-name--concrete { top: 206px; }
  .service-name--sanding { top: 308px; }

  .service-photo {
    position: absolute;
    left: 414px;
    width: 106px;
    height: 72px;
    border: 1px solid #ccc;
    box-shadow: 0 4px 6px rgba(0, 0, 0, 0.45);
  }
  .service-photo--timber {
    top: 128px;
    background: linear-gradient(135deg, var(--tile-red), var(--tile-rose) 50%, var(--tile-red));
  }
  .service-photo--concrete {
    top: 226px;
    background: radial-gradient(ellipse at 40% 60%, var(--concrete-light), var(--concrete) 70%);
  }
  .service-photo--sanding {
    top: 325px;
    background: linear-gradient(160deg, var(--sanded-light), var(--sanded-red) 60%, #5e1f0c);
  }

  .copy {
    font-family: "Open Sans", sans-serif;
    font-weight: 300;
    font-size: 16.5px;
    line-height: 24px;
    color: var(--body-ink);
    margin: 0;
    position: absolute;
  }
  .cover--front .copy {
    left: 37px;
    top: 452px;
    width: 555px;
  }

  .section-title {
    left: 32px;
    font-size: 19px;
    letter-spacing: 5px;
  }
  .section-title--timber { top: 48px; }
  .section-title--concrete { top: 305px; }
  .section-title--sanding { top: 560px; }
  .cover--back .copy {
    left: 47px;
    width: 560px;
  }
  .copy--timber { top: 108px; }
  .copy--concrete { top: 365px; }
  .copy--sanding { top: 620px; }
</style>
</head>
<body>

<header class="brand">
  <span class="brand-mark"></span>
  <span class="brand-name">GRAND OAK SURFACES</span>
</header>

<section class="cover cover--back">
  <div class="cover-art" role="img" aria-label="Warm end-grain timber texture with flowing dark amber drapes"></div>
  <h2 class="section-title section-title--timber">1. Timber Flooring</h2>
  <p class="copy copy--timber">This is sample Text. The resulting slice is true, perfect, vertically grained wood with the annual rings being the evenly distributed Wooden block floors, also known as end block, butcher block and parquet floors have been around as long as someone has had a cross cut saw to cut a tree into rounds or a square beam into blocks. The resulting ‘slice’ is true, perfect, vertically grained wood with the annual rings being the evenly distributed wear surface.</p>
  <h2 class="section-title section-title--concrete">2. Concrete Grinding</h2>
  <p class="copy copy--concrete">This is sample Text. The resulting slice is true, perfect, vertically grained wood with the annual rings being the evenly distributed Wooden block floors, also known as end block, butcher block and parquet floors have been around as long as someone has had a cross cut saw to cut a tree into rounds or a square beam into blocks. The resulting ‘slice’ is true, perfect, vertically grained wood with the annual rings being the evenly distributed wear surface.</p>
  <h2 class="section-title section-title--sanding">3. Floor Sanding</h2>
  <p class="copy copy--sanding">This is sample Text. The resulting slice is true, perfect, vertically grained wood with the annual rings being the evenly distributed Wooden block floors, also known as end block, butcher block and parquet floors have been around as long as someone has had a cross cut saw to cut a tree into rounds or a square beam into blocks. The resulting ‘slice’ is true, perfect, vertically grained wood with the annual rings being the evenly distributed wear surface.</p>
</section>

<section class="cover cover--front">
  <div class="cover-art" role="img" aria-label="End-grain timber block texture fading into dark flowing wood swirls"></div>
  <h1 class="title">Proud to Offer</h1>
  <h2 class="service-name service-name--timber">1.&nbsp;&nbsp; Timber Flooring</h2>
  <div class="service-photo service-photo--timber" role="img" aria-label="Timber parquet floor tiles"></div>
  <h2 class="service-name service-name--concrete">2. Concrete Grinding<br>&amp; Sealing</h2>
  <div class="service-photo service-photo--concrete" role="img" aria-label="Polished and sealed concrete floor"></div>
  <h2 class="service-name service-name--sanding">3. Floor Sanding</h2>
  <div class="service-photo service-photo--sanding" role="img" aria-label="Freshly sanded and finished timber boards"></div>
  <p class="copy">This is sample Text. The resulting slice is true, perfect, vertically grained wood with the annual rings being the evenly distributed Wooden block floors, also known as end block, butcher block and parquet floors have been around as long as someone has had a cross cut saw to cut a tree into rounds or a square beam into blocks. The resulting ‘slice’ is true, perfect, vertically grained wood with the annual rings being the evenly distributed wear surface.</p>
</section>

</body>
</html>
```